Redesign company trifold brochure

We are rebranding our company in September and looking for a more professional design for our brochure.

What we do - providing interdisciplinary care for those supporting ill, elderly and special needs pets at home following the human hospice model of care - is very novel and our brochure is key in explaining it and our offerings.

We serve dogs and cats. Most of the animals are quite sick, elderly. I have many personal and stock photos we can use in the brochure. Please - no pictures of puppies and/or kittens.

The hard part is fitting the info and message into a clear and concise format.

It must be appealing both to pet owners and vets (who are our primary source of patients through referrals).

It should covey WARMTH, COMPASSION, PROFESSIONALISM, and EXPERTISE.

Please look at our website www.QuillbrookAnimalRest.com for more info

We have until now used maroon and copper for colors - to reflect the "sunset" of the pets life. BUT are now changing to Navy, Teal and White to reflect calm, trust and competence.

We will use the same logo recolored.

Existing brochure and new logo are attached.

PLEASE ask questions!!
Updates

We have a library of stock images you are welcome to use. All have been legally acquired and we have the right to use them. You DO NOT have to use them, just sending along in case you wish to. https://www.filecrate.example/sh/kq4mzrt82vplx/BBQ9Trnz-Pydm3hg7aLwRKfZo?dl=0

Our colors are NAVY, TEAL and WHITE. For your reference, the navy we use is 99/87/44/55 (CMYK) The Teal we use is 76/11/44/0 (CMYK) Thank you!

Designers -- pleaseuse pictures of older pets (no puppies or kittens). Below is a link to stock photos we own that would be appropriate for use in the brochure. https://www.filecrate.example/sh/w472fkdl9rzqx/BBTc5EhtyMPLWGVXsdRoF_3k?dl=0 THANK YOU!

Designers -- I would VERY much like to include a photo of a pet in a wheel chair. I have personal photos as well as (purchased) stock photos for this purpose which can be found at http://lnk.example/QARCS-Pets-in-Wheelchairs Thank you!!

Today is the last day! Many of you have submitted beautiful designs and others are rolling in. I am so appreciative of your time and energy!! Please do not let the deadline pass without YOUR very BEST entry being submitted!! Thank you! - Marisol & All of us at Quillbrook Animal Rest & Comfort Services

Target Market(s)

Pet Owners and Veterinarians

Industry/Entity Type

Pet Care

Font styles to use
Serif

Colors
0455a3
33b8a4
ffffff

Requirements
Must have
• Our logo and information about our services. Pictures of pets. Our contact info. PLEASE NOTE: this is a 2 sided brochure. Please submit both inside and outside.
Should not have
• puppies, kittens - anything off message

```html
<!DOCTYPE html>
<html lang="en">
<head>
<meta charset="utf-8">
<title>Quillbrook Animal Rest &amp; Comfort Services – Trifold Brochure</title>
<link href="https://fonts.googleapis.com/css2?family=Marcellus&family=Arimo:wght@400&family=Cormorant+Garamond:ital,wght@1,500&display=swap" rel="stylesheet">
<style>
  :root {
    --teal: #2aa89b;
    --teal-logo: #2fa89a;
    --navy: #0d1f45;
    --arc-blue: #1a5f9e;
    --ink: #1c2a3d;
    --grey: #555a60;
    --white: #ffffff;
    --stage: #e8e5e0;
    --photo-warm-a: #e9cbb8;
    --photo-warm-b: #c9a27a;
    --photo-cat-a: #f3ede6;
    --photo-cat-b: #c9783a;
    --photo-pair-a: #f4f2ef;
    --photo-pair-b: #a8683a;
  }
  * { box-sizing: border-box; margin: 0; padding: 0; }
  html, body { width: 1200px; height: 943px; overflow: hidden; }
  body { background: var(--stage); position: relative; font-family: "Arimo", Arial, sans-serif; }

  .brochure {
    position: absolute; left: 36px; top: 36px; width: 1129px; height: 869px;
    background: var(--white); box-shadow: 0 2px 8px rgba(0,0,0,.18);
  }
  .panel { position: absolute; top: 0; height: 869px; overflow: hidden; }
  .panel--beliefs { left: 0; width: 373px; background: var(--teal); }
  .panel--contact { left: 373px; width: 378px; background: var(--white); }
  .panel--cover { left: 751px; width: 378px; background: var(--white); }
  .panel svg.art { position: absolute; left: 0; top: 0; }

  /* beliefs */
  .beliefs { position: absolute; left: 12px; top: 386px; width: 342px; color: var(--ink); }
  .beliefs__title { font-family: "Marcellus", Georgia, serif; font-weight: 400; font-size: 25px; color: var(--ink); margin-bottom: 4px; }
  .beliefs__list { list-style: none; font-size: 15.5px; line-height: 20px; }
  .beliefs__list li { position: relative; padding-left: 21px; margin-bottom: 11px; text-align: justify; }
  .beliefs__list li::before { content: "•"; position: absolute; left: 3px; top: 0; }

  /* logo lockup */
  .lockup { position: absolute; display: flex; align-items: center; gap: 12px; }
  .lockup__mark { width: 48px; height: 48px; border-radius: 50%; background: var(--teal-logo); flex: none; }
  .lockup__name { font-family: "Marcellus", Georgia, serif; color: var(--navy); font-size: 25px; line-height: 28px; }
  .panel--contact .lockup { left: 62px; top: 520px; }
  .panel--cover .lockup { left: 70px; top: 70px; }

  .tagline {
    position: absolute; left: 0; top: 222px; width: 378px; text-align: center;
    font-family: "Marcellus", Georgia, serif; color: var(--navy); font-size: 26px; line-height: 51px;
  }

  /* contact */
  .contact { position: absolute; left: 0; top: 634px; width: 378px; text-align: center; color: var(--grey); }
  .contact__phone { font-size: 19px; margin-bottom: 11px; }
  .contact__line { font-size: 16px; margin-bottom: 12px; }
  .contact__address { font-size: 15px; line-height: 21px; }
  .contact__rule { position: absolute; left: 15px; top: 791px; width: 353px; height: 1px; background: #333; }
  .social { position: absolute; left: 98px; top: 815px; font-size: 15px; color: var(--grey); line-height: 24px; }
  .social__item { display: flex; align-items: center; gap: 7px; }
  .social__item::before { content: ""; width: 15px; height: 15px; background: var(--arc-blue); border-radius: 2px; }

  .footer-band {
    position: absolute; left: 0; bottom: 0; width: 378px; height: 55px; background: var(--navy);
    display: flex; align-items: center; justify-content: center;
    font-family: "Cormorant Garamond", Georgia, serif; font-style: italic; font-weight: 500;
    color: var(--teal); font-size: 22px;
  }
</style>
</head>
<body>
<main class="brochure">

  <section class="panel panel--beliefs">
    <svg class="art" width="373" height="380" viewBox="0 0 373 380">
      <defs>
        <linearGradient id="warm" x1="0" y1="0" x2="1" y2="1">
          <stop offset="0" stop-color="var(--photo-warm-a)"/>
          <stop offset="1" stop-color="var(--photo-warm-b)"/>
        </linearGradient>
      </defs>
      <path d="M0 0 H373 V205 Q200 330 0 348 Z" fill="url(#warm)" role="img" aria-label="Photo: a golden dog resting its head on a soft plush toy"/>
      <path d="M0 350 Q200 332 373 207" fill="none" stroke="var(--arc-blue)" stroke-width="6"/>
    </svg>
    <div class="beliefs">
      <h2 class="beliefs__title">We Believe</h2>
      <ul class="beliefs__list">
        <li>That animals are conscious beings, capable of thought, feeling, emotion and choice.</li>
        <li>That each animal is an individual with his or her unique needs and whishes.</li>
        <li>That all pets deserve to be pain-free.</li>
        <li>That the principles of human hospice and palliative care are equally powerful when applied to animals</li>
        <li>That an interdisciplinary team is essential to addressing that needs of pets and their families through aging and illness.</li>
        <li>That quality of life is subjective best evaluated by the family who knows and loves the animal.</li>
        <li>That there isn't are answer that is right for every animal or every family</li>
      </ul>
    </div>
  </section>

  <section class="panel panel--contact">
    <svg class="art" width="378" height="330" viewBox="0 0 378 330">
      <defs>
        <linearGradient id="cat" x1="0" y1="0" x2="1" y2="1">
          <stop offset="0" stop-color="var(--photo-cat-a)"/>
          <stop offset="1" stop-color="var(--photo-cat-b)"/>
        </linearGradient>
      </defs>
      <path d="M0 0 H378 V250 Q190 345 0 268 Z" fill="url(#cat)" role="img" aria-label="Photo: an orange cat lying on a red cushion"/>
      <path d="M0 268 Q190 345 378 250" fill="none" stroke="var(--navy)" stroke-width="7"/>
    </svg>
    <div class="lockup">
      <span class="lockup__mark"></span>
      <span class="lockup__name">Quillbrook Animal Rest<br>&amp; Comfort Services</span>
    </div>
    <div class="contact">
      <p class="contact__phone">Contact us (555) 302-QARC</p>
      <p class="contact__line">info@QuillbrookAnimalRest.com</p>
      <p class="contact__line">www.QuillbrookAnimalRest.com</p>
      <p class="contact__address">48 Harbor Mill Road,<br>Suite 210 Fairhaven, Ma 02719</p>
    </div>
    <div class="contact__rule"></div>
    <div class="social">
      <p class="social__item">QuillbrookAnimalRest</p>
      <p class="social__item">QARCSPets</p>
    </div>
  </section>

  <section class="panel panel--cover">
    <div class="lockup">
      <span class="lockup__mark"></span>
      <span class="lockup__name">Quillbrook Animal Rest<br>&amp; Comfort Services</span>
    </div>
    <p class="tagline">Skilled Home Care for Ill,<br>Elderly and Special Needs<br>Animals</p>
    <svg class="art" width="378" height="869" viewBox="0 0 378 869">
      <defs>
        <linearGradient id="pair" x1="0" y1="0" x2="1" y2="0.6">
          <stop offset="0" stop-color="var(--photo-pair-a)"/>
          <stop offset="1" stop-color="var(--photo-pair-b)"/>
        </linearGradient>
      </defs>
      <path d="M0 585 Q110 440 378 432 V814 H0 Z" fill="url(#pair)" role="img" aria-label="Photo: a grey cat sitting beside a brown dachshund"/>
      <path d="M2 580 Q100 420 378 410" fill="none" stroke="var(--arc-blue)" stroke-width="8"/>
    </svg>
    <p class="footer-band">Compassionate Support for Families</p>
  </section>

</main>
</body>
</html>
```